Clear Plastic Card Design

I am looking to have a business card designed from my logo icon. I am looking to match the style of a different business card I have attached in the files.
Looking for a card that is plastic, with layers of transparency in the shape of my logo icon (also attached in the files) - not a circle like the other card. The winning design will incorporate the red icon logo on the front and back and include the charity's name, "Lanterns of Willow Creek" in the same or similar font, as well as an email and phone number. For now, use the email: email@lanternsofwillowcreek.org and the phone number 555-014-7392.
We like how the sample business card has transparency, partial and full opacity layers and a matching color scheme. Files will need to be in vector so that our business card printing company can work with it.
UPDATE:
We've some excellent designs in, thank you everyone! I got an early review from the owner, and he requested a minor redirect to find his perfect design. He wants the design to stand out by NOT being a rectangle. Try instead a circle, square, or best yet - something that falls in the outline of the logo icon, either fully or partially. Thank you, everyone!
Lanterns of Willow Creek text should be incorporated as well as a phone and email.

```html
<!DOCTYPE html>
<html lang="en">
<head>
<meta charset="utf-8">
<title>Lanterns of Willow Creek – Clear Card</title>
<link href="https://fonts.googleapis.com/css2?family=Roboto:wght@400;700&display=swap" rel="stylesheet">
<style>
  :root {
    --backdrop: #e6e1dc;
    --clear-card: rgba(255, 255, 255, 0.55);
    --card-edge: #cfcac6;
    --brand-red: #c8201a;
    --brand-red-deep: #9e0f12;
    --brand-red-light: #e0452f;
    --ink-light: #ffffff;
  }
  html, body {
    margin: 0;
    padding: 0;
    width: 1200px;
    height: 721px;
    overflow: hidden;
    background: var(--backdrop);
  }
  .card-set {
    display: block;
    width: 1200px;
    height: 721px;
  }
  .clear-card { fill: var(--clear-card); stroke: var(--card-edge); stroke-width: 2; }
  .brand-name { font-family: "Roboto", Arial, sans-serif; font-weight: 700; fill: var(--brand-red); }
  .contact-line { font-family: "Roboto", Arial, sans-serif; fill: var(--ink-light); }
  .contact-phone { font-weight: 700; font-size: 13px; letter-spacing: 1px; }
  .contact-email { font-weight: 400; font-size: 10px; letter-spacing: 0.6px; }
  .holder-name { font-family: "Roboto", Arial, sans-serif; font-weight: 700; font-size: 15px; fill: var(--ink-light); }
  .verse-ref { font-family: "Roboto", Arial, sans-serif; font-weight: 700; font-size: 12px; fill: var(--ink-light); }
</style>
</head>
<body>
<svg class="card-set" viewBox="0 0 1200 721" xmlns="http://www.w3.org/2000/svg">
  <defs>
    <linearGradient id="red-panel" x1="0" y1="0" x2="1" y2="1">
      <stop offset="0" stop-color="var(--brand-red-light)"/>
      <stop offset="0.55" stop-color="var(--brand-red)"/>
      <stop offset="1" stop-color="var(--brand-red-deep)"/>
    </linearGradient>
  </defs>

  <!-- Front card -->
  <g class="card-front">
    <rect class="clear-card" x="245" y="180" width="335" height="330" rx="32"/>
    <rect x="290" y="262" width="34" height="34" fill="url(#red-panel)"/>
    <text class="brand-name" x="290" y="345" font-size="30">LANTERNS OF</text>
    <text class="brand-name" x="290" y="381" font-size="30">WILLOW CREEK</text>
  </g>

  <!-- Back card -->
  <g class="card-back">
    <rect class="clear-card" x="620" y="180" width="335" height="330" rx="32"/>
    <rect x="645" y="205" width="285" height="280" rx="20" fill="url(#red-panel)" opacity="0.92"/>
    <text class="verse-ref" x="688" y="403">Isaiah 61:1</text>
    <g transform="translate(810 412) rotate(-90)">
      <text class="contact-line contact-phone" x="0" y="0">PH: 555-014-7392</text>
      <text class="contact-line contact-email" x="-30" y="18">email@lanternsofwillowcreek.org</text>
    </g>
    <text class="holder-name" transform="translate(922 362) rotate(-90)">MARCUS HALE</text>
  </g>
</svg>
</body>
</html>
```